IT Freelancer (Consulting, trainer and project manager) needed letterhead

As a freelancer for IT Trainingswhip, consulting and project management I need a letterhead design. What is desired is a design that fits the existing logo (see Annex). It is functional, reliable, and equal time wirkenn Agil and modern. The whole is in color, as well as printed out to make a good impression on a black and white printer. The whole is to the existing Cooperate design (business card, homepage, logo) fit. Therefore, the choice of colors.
Updates

Target Market(s)

Customers such as medium-sized enterprises, training institutions

Industry/Entity Type

Consulting

Colors
0455a3
3277b5
85abd2
cfdfed
34a6d7
32a6d6
249fd4
0792cd
85cae6

Requirements
Must have
• Must include logo (see Annex) address (Brennerweg 14, 93471 Lindenhain, Germany). Must seriously and act simultaneously Agil. Design should (even) be adaptable (signature, address, etc.) design must look good on a black / white laser

```html
<!DOCTYPE html>
<html lang="en">
<head>
<meta charset="utf-8">
<title>Konrad Feldmann – Letterhead</title>
<link rel="stylesheet" href="https://fonts.googleapis.com/css2?family=Montserrat:wght@700&family=Lato:ital,wght@1,400&display=swap">
<style>
  :root {
    --backdrop: #626262;
    --paper: #ffffff;
    --blue-dark: #0455a3;
    --blue-light: #34a6d7;
    --watermark: #f5f5f5;
    --footer-text: #5a5a5a;
  }
  html, body {
    margin: 0;
    width: 800px;
    height: 1200px;
    overflow: hidden;
    background: var(--backdrop);
  }
  .sheet {
    position: absolute;
    left: 107px;
    top: 161px;
    width: 586px;
    height: 879px;
    background: var(--paper);
    overflow: hidden;
  }
  .header {
    position: absolute;
    left: 0; top: 0;
    width: 100%;
    height: 123px;
    background: var(--blue-light);
  }
  .header-band {
    position: absolute;
    left: 81px; top: 22px;
    right: 0; bottom: 0;
    background: var(--blue-dark);
  }
  .mark-circle {
    position: absolute;
    left: 31px; top: 24px;
    width: 94px; height: 94px;
    border-radius: 50%;
    background: var(--blue-light);
    border: 3px solid var(--blue-dark);
  }
  .wordmark {
    position: absolute;
    left: 152px; top: 47px;
    margin: 0;
    color: var(--paper);
    font-family: "Montserrat", sans-serif;
    font-weight: 700;
    text-align: center;
    line-height: 1;
  }
  .wordmark .first { display: block; font-size: 28px; letter-spacing: 0.5px; }
  .wordmark .last { display: block; font-size: 22px; letter-spacing: 3.5px; margin-top: 4px; }
  .watermark {
    position: absolute;
    left: 81px; top: 227px;
  }
  .footer {
    position: absolute;
    left: 0; top: 826px;
    width: 100%;
    height: 16px;
  }
  .footer-bars {
    position: absolute;
    left: 0; top: 0;
  }
  .footer-address {
    position: absolute;
    left: 0; right: 0; top: 0;
    margin: 0;
    text-align: center;
    font-family: "Lato", sans-serif;
    font-style: italic;
    font-size: 10.5px;
    line-height: 16px;
    color: var(--footer-text);
    text-transform: uppercase;
    letter-spacing: -0.1px;
  }
</style>
</head>
<body>
  <main class="sheet">
    <header class="header">
      <div class="header-band"></div>
      <div class="mark-circle"></div>
      <h1 class="wordmark"><span class="first">KONRAD</span><span class="last">FELDMANN</span></h1>
    </header>

    <svg class="watermark" width="424" height="424" viewBox="0 0 424 424" aria-hidden="true">
      <circle cx="212" cy="212" r="199" fill="none" stroke="var(--watermark)" stroke-width="26"/>
    </svg>

    <footer class="footer">
      <svg class="footer-bars" width="586" height="16" viewBox="0 0 586 16" aria-hidden="true">
        <polygon points="0,4 173,4 169,12 0,12" fill="var(--blue-dark)"/>
        <polygon points="417,4 586,4 586,12 413,12" fill="var(--blue-light)"/>
      </svg>
      <p class="footer-address">Brennerweg 14, 93471 Lindenhain, Germany</p>
    </footer>
  </main>
</body>
</html>
```